Hopyard Specials socials

Hello - simular to last project but for a different venue.

Specials are:
$5 @ 5pm - $5 Pints Wednesday - Sunday.
Wednesday $1 Chicken Wings
Thursday - $12.50 Pizzas
Friday $12.48 Pint & Burger 12-3pm
Kids Eat Free - Saturdays & Sundays 12-3pm

Need an instagram image for each special and also a combined Facebook cover.
Needs to be classy but playful

```html
<!DOCTYPE html>
<html lang="en">
<head>
<meta charset="utf-8">
<title>Hopyard – Pizza Thursday</title>
<link rel="stylesheet" href="https://fonts.googleapis.com/css2?family=Montserrat:wght@300;500;800&family=Rubik+Dirt&display=swap">
<style>
  :root {
    --stage: #8c8c8c;
    --wall-deep: #3a1215;
    --wall: #5a2226;
    --wood-light: #a08a70;
    --wood-dark: #6e5a46;
    --crust: #d9a35a;
    --cheese: #f1d79a;
    --sauce: #c6562e;
    --promo-red: #e60000;
    --white: #ffffff;
    --black: #000000;
  }
  * { margin: 0; padding: 0; box-sizing: border-box; }
  html, body { width: 692px; height: 1200px; overflow: hidden; }
  body { background: var(--stage); position: relative; font-family: "Montserrat", sans-serif; }

  .special-post {
    position: absolute; left: 46px; top: 300px;
    width: 600px; height: 600px; overflow: hidden;
  }
  .backdrop {
    position: absolute; inset: 0;
    background:
      linear-gradient(180deg, var(--wall-deep) 0%, var(--wall) 45%, var(--wall) 62%, var(--wood-dark) 63%, var(--wood-light) 85%, var(--wood-dark) 100%);
  }
  .venue-name {
    position: absolute; left: 22px; top: 52px;
    font-family: "Montserrat", sans-serif; font-weight: 800;
    font-size: 13px; letter-spacing: 1px; color: var(--white);
  }
  .headline { position: absolute; left: 162px; top: 40px; width: 279px; height: 82px; }
  .headline text { font-family: "Rubik Dirt", sans-serif; fill: var(--white); }
  .day-pill {
    position: absolute; left: 217px; top: 141px; width: 165px; height: 40px;
    background: var(--promo-red); border: 2px solid var(--white); border-radius: 20px;
    color: var(--white); font-weight: 800; font-size: 24px;
    display: flex; align-items: center; justify-content: center; letter-spacing: 0.3px;
  }
  .pizza-photo {
    position: absolute; left: 34px; top: 215px; width: 437px; height: 336px;
    border-radius: 50%; transform: rotate(-8deg);
    background: radial-gradient(ellipse at 50% 45%, var(--cheese) 0%, #e8b870 40%, var(--sauce) 62%, var(--crust) 75%, #c9a070 88%, #b89468 100%);
  }
  .price-bubble { position: absolute; left: 440px; top: 218px; width: 125px; height: 135px; }
  .price-bubble text { font-family: "Montserrat", sans-serif; font-weight: 500; fill: var(--white); }
  .offer-band {
    position: absolute; left: 0; bottom: 0; width: 600px; height: 33px;
    background: var(--black); color: var(--white);
    font-weight: 300; font-size: 20px; letter-spacing: 0.5px;
    display: flex; align-items: center; justify-content: center;
  }
</style>
</head>
<body>
  <section class="special-post">
    <div class="backdrop" role="img" aria-label="Dark red textured wall above a wooden tabletop, scattered with herbs and pepper rings"></div>
    <div class="venue-name">HOPYARD</div>
    <svg class="headline" viewBox="0 0 279 82">
      <text x="0" y="76" font-size="92" textLength="279" lengthAdjust="spacingAndGlyphs">PIZZAS</text>
    </svg>
    <div class="day-pill">THURSDAY</div>
    <div class="pizza-photo" role="img" aria-label="Seafood pizza with prawns, crab sticks, squid and peppers on a wooden board"></div>
    <svg class="price-bubble" viewBox="0 0 125 135">
      <path d="M66 4 a54 54 0 1 1 -20 104 C30 122 18 128 3 131 C14 120 20 110 18 96 A54 54 0 0 1 66 4 Z"
            fill="var(--promo-red)" stroke="var(--white)" stroke-width="1.6" stroke-dasharray="5 3"/>
      <text x="66" y="67" font-size="25" text-anchor="middle">$12.50</text>
    </svg>
    <div class="offer-band">Kids Eat Free - Saturdays &amp; Sundays 12-3pm</div>
  </section>
</body>
</html>
```